Brell Harbor Company Business Cards

Front and Back Business Card - logo and text setup - cool design. I need workable photoshop or illustrator files so I can setup each employee card with design that is created
Updates

Hi everyone, thank you for the great entries. Please no more white and blue cards - there are so many already - black and silver only now please. thanks!

Target Market(s)

Construction Industry - Facility Managers

Industry/Entity Type

Construction

Contact Information for Business Card

I really like contemporary simplistic looks - clean neat....not opposed to seeing some black backrounds

Requirements
Must have
• Logo/website address with design on front only - www.brellharbor-example.com (logo attached)
• Back:
• Name/Title/Company Address/Phone/email address
Nice to have
• Cool design
Should not have
• Nothing gimmicky like Fire or Water - since we are a Fire Protection company - it has all been done

```html
<!DOCTYPE html>
<html lang="en">
<head>
<meta charset="utf-8">
<title>Brell Harbor Company – Business Cards</title>
<link rel="stylesheet" href="https://fonts.googleapis.com/css2?family=Montserrat:wght@300;400;700&family=Open+Sans:wght@400;600&display=swap">
<style>
  :root {
    --backdrop: #262626;
    --card: #151515;
    --ink-white: #f2f2f2;
    --accent-red: #e8492f;
    --accent-blue: #27427e;
  }
  * { box-sizing: border-box; margin: 0; padding: 0; }
  html, body {
    width: 1200px; height: 900px; overflow: hidden;
    background: var(--backdrop);
  }
  .sheet {
    position: relative; width: 1200px; height: 900px;
  }
  .card {
    position: absolute; left: 270px;
    width: 660px; height: 377px;
    background: var(--card);
    box-shadow: 0 10px 30px rgba(0,0,0,0.45);
  }
  .card--front { top: 58px; }
  .card--back { top: 465px; }

  /* Front */
  .front-wordmark {
    position: absolute; left: 0; right: 0; top: 140px;
    text-align: center;
    font-family: "Montserrat", sans-serif; font-weight: 700;
    font-size: 40px; letter-spacing: -0.5px;
    color: var(--accent-red);
  }
  .front-website {
    position: absolute; left: 0; right: 0; top: 262px;
    text-align: center;
    font-family: "Open Sans", sans-serif; font-size: 14px;
    color: var(--accent-red);
  }

  /* Back */
  .holder {
    position: absolute; left: 58px; top: 108px;
  }
  .holder-name {
    font-family: "Montserrat", sans-serif; font-size: 27px;
    color: var(--ink-white); letter-spacing: 0.5px; line-height: 1;
  }
  .holder-name .first { font-weight: 300; }
  .holder-name .last { font-weight: 700; }
  .holder-title {
    margin-top: 4px;
    font-family: "Montserrat", sans-serif; font-weight: 700;
    font-size: 11px; color: var(--accent-red); letter-spacing: 0.3px;
  }
  .divider {
    position: absolute; left: 58px; top: 160px;
    width: 348px; height: 2px; background: var(--accent-blue);
  }
  .contact-list {
    position: absolute; left: 58px; top: 172px;
    list-style: none;
    font-family: "Open Sans", sans-serif; font-size: 15px;
    color: var(--ink-white); line-height: 1.25;
  }
  .contact-list li {
    display: flex; align-items: flex-start; gap: 10px; margin-bottom: 9px;
  }
  .contact-list svg { flex: none; margin-top: 2px; }
  .back-wordmark {
    position: absolute; right: 48px; top: 180px;
    font-family: "Montserrat", sans-serif; font-weight: 700;
    font-size: 27px; letter-spacing: -0.3px;
    color: var(--accent-red);
  }
</style>
</head>
<body>
<main class="sheet">
  <section class="card card--front" aria-label="Card front">
    <p class="front-wordmark">Brell Harbor Company</p>
    <p class="front-website">www.brellharbor-example.com</p>
  </section>

  <section class="card card--back" aria-label="Card back">
    <div class="holder">
      <h1 class="holder-name"><span class="first">YOUR</span> <span class="last">NAME</span></h1>
      <p class="holder-title">JOB TITLE</p>
    </div>
    <div class="divider"></div>
    <ul class="contact-list">
      <li>
        <svg width="16" height="14" viewBox="0 0 16 14" aria-hidden="true">
          <path d="M1 4 Q8 -1 15 4 L13 6 L11 4.5 L5 4.5 L3 6 Z" fill="var(--accent-red)"/>
          <rect x="3" y="7" width="10" height="6" rx="1" fill="var(--accent-red)"/>
        </svg>
        <span>000 000 0000</span>
      </li>
      <li>
        <svg width="16" height="14" viewBox="0 0 16 14" aria-hidden="true">
          <rect x="1" y="2" width="14" height="10" fill="var(--accent-red)"/>
          <path d="M1 2 L8 8 L15 2" fill="none" stroke="var(--card)" stroke-width="1.3"/>
        </svg>
        <span>youremail@xyz.com</span>
      </li>
      <li>
        <svg width="16" height="16" viewBox="0 0 16 16" aria-hidden="true">
          <circle cx="8" cy="8" r="6.5" fill="none" stroke="var(--accent-red)" stroke-width="1.3"/>
          <ellipse cx="8" cy="8" rx="2.8" ry="6.5" fill="none" stroke="var(--accent-red)" stroke-width="1"/>
          <line x1="1.5" y1="8" x2="14.5" y2="8" stroke="var(--accent-red)" stroke-width="1"/>
        </svg>
        <span>Somewhere, Anywhere<br>City, ST 0000</span>
      </li>
    </ul>
    <p class="back-wordmark">Brell Harbor Company</p>
  </section>
</main>
</body>
</html>
```